Dalvo Kin Business card Design

we need a business card design that is modern , easy to read , and remember able. the business sells all aspects of cooking and cooling equipment for restaurants, bars, cafe and large domestic kitchens
our website : www.dalvokingroup.com

Industry/Entity Type

Cooking

```html
<!DOCTYPE html>
<html lang="en">
<head>
<meta charset="utf-8">
<title>Dalvo Kin Business Card</title>
<link href="https://fonts.googleapis.com/css2?family=Open+Sans:wght@400;600;700&display=swap" rel="stylesheet">
<style>
  :root {
    --bg: #e9e7e3;
    --card: #ffffff;
    --blue: #1ba1e2;
    --red: #e2464d;
    --ink: #4a4a4a;
    --ink-soft: #666666;
    --divider: #f0a3a6;
  }
  * { margin: 0; padding: 0; box-sizing: border-box; }
  html, body {
    width: 1200px; height: 900px; overflow: hidden;
    background: var(--bg);
    font-family: "Open Sans", Arial, sans-serif;
  }
  .card {
    position: absolute; left: 100px; top: 164px;
    width: 1000px; height: 572px;
    background: var(--card);
    box-shadow: 0 6px 24px rgba(0,0,0,0.15);
  }
  .person { position: absolute; left: 80px; top: 66px; }
  .person-name {
    font-size: 36px; font-weight: 700; color: var(--blue); line-height: 1.1;
  }
  .person-title {
    font-size: 20px; font-weight: 600; color: var(--ink-soft); margin-top: 2px;
  }
  .brand {
    position: absolute; right: 80px; top: 118px; text-align: center;
  }
  .brand-name {
    font-size: 56px; font-weight: 700; color: var(--blue);
    letter-spacing: 2px; line-height: 1;
  }
  .brand-company {
    font-size: 22px; font-weight: 400; color: var(--ink);
    letter-spacing: 3px; margin-top: 16px;
  }
  .contact-row {
    position: absolute; left: 60px; right: 60px; top: 368px;
    display: flex; align-items: flex-start;
  }
  .address {
    width: 270px; font-size: 22px; line-height: 1.3; color: var(--ink);
    font-style: italic;
  }
  .divider {
    width: 1px; height: 104px; background: var(--divider); margin: 0 36px;
  }
  .contact-list { list-style: none; font-size: 22px; color: var(--ink); }
  .contact-list li { display: flex; align-items: center; gap: 14px; line-height: 1.35; }
  .contact-list svg { width: 18px; height: 18px; fill: var(--blue); flex: none; }
  .phones { width: 230px; }
  .online { margin-left: 20px; padding-top: 26px; }
  .online li { line-height: 1.55; }
  .band { position: absolute; left: 0; right: 0; bottom: 0; height: 14px; display: flex; }
  .band-red { width: 320px; background: var(--red); }
  .band-blue { flex: 1; background: var(--blue); margin-left: 4px; }
</style>
</head>
<body>
  <div class="card">
    <div class="person">
      <div class="person-name">Naree Sukjaroen</div>
      <div class="person-title">Managing Director</div>
    </div>

    <div class="brand">
      <div class="brand-name">DALVO KIN</div>
      <div class="brand-company">DALVO KIN GROUP CO.,LTD</div>
    </div>

    <div class="contact-row">
      <p class="address">2150-2188 Charoen Road, Bang Kho, Chom Thong, Bangkok 10150</p>
      <div class="divider"></div>
      <ul class="contact-list phones">
        <li><svg viewBox="0 0 24 24" aria-hidden="true"><path d="M6.6 10.8a15.1 15.1 0 0 0 6.6 6.6l2.2-2.2a1 1 0 0 1 1-.25 11.4 11.4 0 0 0 3.6.57 1 1 0 0 1 1 1V20a1 1 0 0 1-1 1A17 17 0 0 1 3 4a1 1 0 0 1 1-1h3.5a1 1 0 0 1 1 1c0 1.25.2 2.45.57 3.6a1 1 0 0 1-.25 1z"/></svg>020-5550147</li>
        <li><svg viewBox="0 0 24 24" aria-hidden="true"><path d="M7 2h10a2 2 0 0 1 2 2v16a2 2 0 0 1-2 2H7a2 2 0 0 1-2-2V4a2 2 0 0 1 2-2zm0 3v13h10V5zm5 14.2a1 1 0 1 0 0 .01z"/></svg>020-5550147</li>
        <li><svg viewBox="0 0 24 24" aria-hidden="true"><path d="M7 2h8l3 3v4h1a3 3 0 0 1 3 3v7h-4v3H6v-3H2v-7a3 3 0 0 1 3-3h2zm2 2v5h7V6h-2V4zm-1 12v4h8v-4z"/></svg>020-5550147</li>
      </ul>
      <div class="divider"></div>
      <ul class="contact-list online">
        <li><svg viewBox="0 0 24 24" aria-hidden="true"><path d="M3 5h18v14H3zm2 2v.4l7 4.6 7-4.6V7zm0 2.8V17h14V9.8l-7 4.6z"/></svg>info@dalvokingroup.com</li>
        <li><svg viewBox="0 0 24 24" aria-hidden="true"><path d="M12 2a10 10 0 1 0 0 20 10 10 0 0 0 0-20zm6.9 9h-3a15 15 0 0 0-1.3-5.6A8 8 0 0 1 18.9 11zM12 4.1c.9 1.2 1.8 3.6 1.9 6.9h-3.8c.1-3.3 1-5.7 1.9-6.9zM9.4 5.4A15 15 0 0 0 8.1 11h-3a8 8 0 0 1 4.3-5.6zM5.1 13h3a15 15 0 0 0 1.3 5.6A8 8 0 0 1 5.1 13zm6.9 6.9c-.9-1.2-1.8-3.6-1.9-6.9h3.8c-.1 3.3-1 5.7-1.9 6.9zm2.6-1.3a15 15 0 0 0 1.3-5.6h3a8 8 0 0 1-4.3 5.6z"/></svg>www.dalvokingroup.com</li>
      </ul>
    </div>

    <div class="band">
      <div class="band-red"></div>
      <div class="band-blue"></div>
    </div>
  </div>
</body>
</html>
```